job report

Designer – Professional Plumbing Job Report Template

Overview

We are seeking a skilled designer to create a professional, easy-to-use Job Report template for a commercial and maintenance plumbing business.
The report will be used for clients, property managers, facilities managers, strata, and retail centres and must clearly communicate findings, works completed, and recommendations in a polished, compliant, and branded format.

The final document must be suitable for PDF delivery, email, and ongoing reuse.

Objectives

Present plumbing works in a clear, professional, and defensible report format

Improve client understanding of findings and recommendations

Provide a repeatable template that can be used across maintenance, reactive, and investigative works

Allow easy insertion of text, tables, and photos

Report Structure (Minimum Inclusions)
1. Cover Page

Company logo and branding

Report title (e.g. Plumbing Job Report / Investigation Report)

Client name

Site address

Job reference / work order number

Date of attendance

Technician / contractor name

2. Client & Site Details

Client / company name

Site address

Contact person

Contact details

Access notes (after-hours, tenant access, etc.)

3. Reason for Attendance

Clear description of why attendance was required

Call-out type (reactive, scheduled maintenance, investigation, emergency, etc.)

Reported issue or scope requested by client

4. Findings / Observations

Detailed findings discovered on site

Condition of pipework, fixtures, drainage, or systems

Any contributing factors identified

Notes on compliance, wear, damage, or risk

(This section should support bullet points and paragraphs.)

5. Works Carried Out

Step-by-step description of works completed

Equipment used (e.g. jetter, CCTV camera, leak detection, flex shaft, etc.)

Repairs, replacements, testing, and verification

Confirmation that systems were tested and operational on completion

6. Photos & Visual Evidence

Clearly labelled photo sections

Before / during / after photos

Space for photo captions and explanations

Logical layout that aligns photos with written findings

7. Recommendations

Clearly separated from works completed

Urgent vs non-urgent recommendations

Preventative maintenance advice

Upgrade or replacement suggestions

Risk-based language where appropriate

8. Limitations & Exclusions

Areas not inspected

Access limitations

Assumptions made during inspection

Items outside scope of works

9. Conclusion

Summary of outcome

Confirmation of current system status

Next steps (if any)

10. Sign-Off

Contractor / technician name

Company name

Date

Optional client acknowledgement section

Design Requirements

Clean, professional layout

Commercial / trade-appropriate styling (not overly creative)

Easy-to-read fonts

Consistent headings and spacing

Logical flow for busy property managers

Editable format (Word / review badge Docs / InDesign source file)

Final export-ready PDF version

Bonus (Nice to Have)

Traffic-light system (Green / Amber / Red) for condition reporting

Iconography for findings, repairs, and recommendations

Optional sections for compliance notes (AS/NCC references)

Space for QR codes or job reference numbers

Deliverables

Editable master report template

PDF version

Instructions or notes for ongoing use

```html
<!DOCTYPE html>
<html lang="en">
<head>
<meta charset="utf-8">
<title>KPR Plumbing – Job Report Template</title>
<link href="https://fonts.googleapis.com/css2?family=Montserrat:wght@400;500;600;700;800&display=swap" rel="stylesheet">
<style>
:root{
  --board:#b8b7bc;
  --navy:#1b3a5c;
  --navy-deep:#142d4a;
  --cyan:#29bfe6;
  --sheet:#ffffff;
  --field:#ececee;
  --rule:#c9c9cd;
  --ink:#2a2a2e;
  --label:#5a5a60;
}
*{box-sizing:border-box;margin:0;padding:0}
html,body{width:1200px;height:2334px;overflow:hidden}
body{background:var(--board);font-family:'Montserrat',sans-serif;color:var(--ink);position:relative}
.spread{position:absolute;background:#fff;box-shadow:0 1px 3px rgba(0,0,0,.15)}
.page{position:absolute;top:10px;bottom:10px;background:var(--sheet);border:1px solid #d6d6da;padding:0 10px 8px;display:flex;flex-direction:column;overflow:hidden}
.band{margin:8px -10px 3px;height:19px;display:flex;align-items:center;padding-left:12px;color:#fff;font-weight:600;font-size:8.5px;background:linear-gradient(90deg,var(--navy-deep) 0%,var(--navy) 45%,var(--cyan) 100%)}
.band.first{margin-top:12px}
.label{font-size:4.6px;color:var(--label);margin:4px 0 3px}
.bar{height:13px;background:var(--field)}
.lines{background:var(--field) repeating-linear-gradient(180deg,transparent 0 7px,var(--rule) 7px 8px);background-clip:content-box;padding:4px 8px}
.checks{display:grid;grid-template-columns:1fr 1fr;gap:3px 6px;font-size:4.6px;color:var(--label);margin:3px 0 3px 18px}
.checks span::before{content:"";display:inline-block;width:6px;height:6px;border:1px solid #888;margin-right:3px;vertical-align:middle}
.page-label{position:absolute;font-weight:600;font-size:21px;color:#4b4b50;letter-spacing:.5px}
.photo-grid{position:relative;flex:1}
.photo-grid svg{position:absolute}
.cap{position:absolute;font-size:4.6px;color:var(--label)}
.caplines{position:absolute}
/* cover */
.cover-left{position:absolute;left:12px;top:10px;width:243px;height:338px;background:linear-gradient(180deg,#fff 0%,#fff 26%,#6fd3ef 48%,var(--cyan) 58%,var(--navy) 86%)}
.supplier-grid{display:grid;grid-template-columns:repeat(3,1fr);gap:16px 8px;padding:20px 10px 0;text-align:center;font-weight:700;font-size:11px;color:var(--navy)}
.company-name{text-align:center;color:#fff;font-weight:700;line-height:1;white-space:nowrap}
.service-band{position:absolute;left:0;right:0;bottom:34px;height:20px;background:var(--cyan);color:#fff;font-size:6.6px;font-weight:600;display:flex;align-items:center;justify-content:center}
.suburbs{position:absolute;left:8px;right:8px;bottom:4px;display:flex;justify-content:space-between;font-size:4.6px;color:#fff;line-height:1.2}
.cover-right{position:absolute;left:263px;top:10px;width:242px;height:338px;background:var(--navy)}
.ph{position:absolute;background:linear-gradient(135deg,#9aa0a6,#c8c4bd)}
.headline{position:absolute;left:38px;bottom:28px;color:#fff;font-weight:700;font-size:13px;line-height:1.15}
/* page 10 */
.why-head{font-size:11.5px;font-weight:700;color:var(--navy);margin:6px 0 3px 4px}
.why-bar{background:var(--navy);color:#7fd8f2;font-size:6.6px;font-weight:600;padding:3px 8px;width:180px;margin-top:6px}
.why-text{font-size:4.6px;color:var(--label);line-height:1.35;margin:3px 0 0 28px}
.badges{display:flex;justify-content:space-around;align-items:center;margin-top:auto;padding-bottom:10px}
.badges i{display:block;width:30px;height:14px;background:#d5dbe3;border-radius:3px}
.badges i.c{width:22px;height:22px;border-radius:50%;background:#5bb8e8}
</style>
</head>
<body>

<!-- Cover spread -->
<section class="spread" style="left:665px;top:28px;width:510px;height:358px">
  <div class="cover-left">
    <div class="supplier-grid">
      <span>Hotline</span><span>Flamo</span><span>Pipeline</span>
      <span>Vexa</span><span>Rivo</span><span>AquaPeak</span>
      <span>Thermo</span><span>Clara</span><span>Fixa</span>
    </div>
    <div class="company-name" style="position:absolute;top:236px;left:0;right:0;font-size:26px">KPR Plumbing</div>
    <div class="service-band">Servicing the Sutherland Shire, St George &amp; Sydney areas</div>
    <div class="suburbs">
      <div>Caringbah<br>Heathcote<br>Miranda<br>Taren Point</div>
      <div>Caringbah South<br>Illawong<br>Oyster Bay<br>Waterfall</div>
      <div>Como<br>Jannali<br>Sutherland<br>Yowie Bay</div>
      <div>Cronulla<br>Kirrawee<br>Sylvania<br>Plus much more...</div>
      <div>Engadine<br>Loftus<br>Sylvania Waters</div>
      <div>Gymea<br>Menai</div>
    </div>
  </div>
  <div class="cover-right">
    <div class="company-name" style="padding-top:24px;font-size:20px">KPR Plumbing</div>
    <div class="ph" role="img" aria-label="Gas cooktop installation" style="left:12px;top:68px;width:70px;height:54px"></div>
    <div class="ph" role="img" aria-label="Tap fitting" style="left:86px;top:68px;width:70px;height:54px"></div>
    <div class="ph" role="img" aria-label="Freestanding bath" style="left:160px;top:68px;width:70px;height:54px"></div>
    <div class="ph" role="img" aria-label="Vessel basin" style="left:12px;top:126px;width:70px;height:60px"></div>
    <div class="ph" role="img" aria-label="Blocked drain" style="left:86px;top:126px;width:70px;height:60px"></div>
    <div class="ph" role="img" aria-label="Pipework under sink" style="left:160px;top:126px;width:70px;height:60px"></div>
    <div class="ph" role="img" aria-label="Copper pipework" style="left:12px;top:190px;width:70px;height:56px"></div>
    <div class="ph" role="img" aria-label="Hot water unit" style="left:86px;top:190px;width:70px;height:56px"></div>
    <div class="ph" role="img" aria-label="Plumbing job site" style="left:160px;top:190px;width:70px;height:56px"></div>
    <div role="img" aria-label="Portrait of the plumber" style="position:absolute;left:150px;top:218px;width:78px;height:120px;background:linear-gradient(180deg,#3d5a7a,#22344d);border-radius:36px 36px 0 0"></div>
    <div class="headline">SYDNEY'S<br>TRUSTED<br>PLUMBING<br>SPECIALISTS</div>
  </div>
</section>

<!-- Pages 1–2 -->
<section class="spread" style="left:663px;top:508px;width:512px;height:357px">
  <div class="page" style="left:12px;width:243px">
    <div class="band first">Plumbing Job Report / Investigation Report</div>
    <div class="label">Client name</div><div class="bar"></div>
    <div class="label">Site address</div><div class="bar"></div>
    <div class="label">Job reference / work order number</div><div class="bar"></div>
    <div class="label">Date of attendance</div><div class="bar"></div>
    <div class="label">Technician / contractor name</div><div class="bar"></div>
    <div class="band">Client &amp; Site Details</div>
    <div class="label">Client / company name</div><div class="bar"></div>
    <div class="label">Site address</div><div class="bar"></div>
    <div class="label">Contact person</div><div class="bar"></div>
    <div class="label">Contact details</div><div class="lines" style="height:32px"></div>
    <div class="label">Access notes (after-hours, tenant access, etc.</div><div class="lines" style="height:30px"></div>
  </div>
  <div class="page" style="left:262px;width:243px;border-right:none">
    <div class="band first">Reason for Attendance</div>
    <div class="label">Clear description of why attendance was required</div><div class="lines" style="height:42px"></div>
    <div class="label">Call-out type</div>
    <div class="checks"><span>Reactive,</span><span>Scheduled Maintenance</span><span>Investigation,</span><span>Emergency, etc.)</span></div>
    <div class="label">Reported issue or scope requested by client</div><div class="lines" style="height:32px"></div>
    <div class="band">Findings / Observations</div>
    <div class="label">Detailed findings discovered on site</div><div class="lines" style="height:38px"></div>
    <div class="label">Condition of pipework, fixtures, drainage, or systems</div><div class="lines" style="height:26px"></div>
    <div class="label">Any contributing factors identified</div><div class="lines" style="height:26px"></div>
    <div class="label">Notes on compliance, wear, damage, or risk</div><div class="lines" style="height:26px"></div>
  </div>
</section>
<div class="page-label" style="left:766px;top:884px">Page 1</div>
<div class="page-label" style="left:1012px;top:884px">Page 2</div>

<!-- Pages 3–4 -->
<section class="spread" style="left:663px;top:987px;width:512px;height:358px">
  <div class="page" style="left:12px;width:243px">
    <div class="band first">Works Carried Out</div>
    <div class="label">Step-by-step description of works completed</div><div class="lines" style="height:88px"></div>
    <div class="label">Equipment used (e.g</div>
    <div class="checks"><span>Jetter,</span><span>CCTV Camera,</span><span>Leak Detection,</span><span>Flex Shaft, etc.)</span><span>Repairs,</span><span>Replacements</span><span>Testing</span><span>Verification</span></div>
    <div class="label">Confirmation that systems were tested and operational on completion</div><div class="lines" style="flex:1"></div>
  </div>
  <div class="page" style="left:262px;width:243px;border-right:none">
    <div class="band first">Photos &amp; Visual Evidence</div>
    <div class="label">Clearly labelled photo sections</div>
    <div class="photo-grid">
      <svg width="230" height="290" viewBox="0 0 230 290" style="left:-6px;top:0">
        <g fill="#fff" stroke="#8a8a8f" stroke-width="1.2">
          <rect x="8" y="8" width="100" height="104" rx="12" transform="rotate(-8 58 60)"/>
          <rect x="122" y="8" width="100" height="104" rx="12" transform="rotate(-8 172 60)"/>
          <rect x="10" y="170" width="100" height="122" rx="12" transform="rotate(-6 60 230)"/>
        </g>
      </svg>
      <div class="cap" style="left:2px;top:118px">Before</div>
      <div class="lines caplines" style="left:0;top:124px;width:108px;height:30px"></div>
      <div class="cap" style="left:114px;top:118px">During</div>
      <div class="lines caplines" style="left:112px;top:124px;width:112px;height:30px"></div>
      <div class="cap" style="left:124px;top:168px">After</div>
      <div class="lines caplines" style="left:122px;top:174px;width:102px;height:114px"></div>
    </div>
  </div>
</section>
<div class="page-label" style="left:778px;top:1362px">Page 3</div>
<div class="page-label" style="left:1022px;top:1362px">Page 4</div>

<!-- Pages 5–6 -->
<section class="spread" style="left:663px;top:1466px;width:514px;height:359px">
  <div class="page" style="left:10px;width:245px">
    <div class="band first">Photos &amp; Visual Evidence</div>
    <div class="label">Clearly labelled photo sections</div>
    <div class="photo-grid">
      <svg width="230" height="290" viewBox="0 0 230 290" style="left:-6px;top:0">
        <g fill="#fff" stroke="#8a8a8f" stroke-width="1.2">
          <rect x="8" y="8" width="100" height="104" rx="12" transform="rotate(-8 58 60)"/>
          <rect x="122" y="8" width="100" height="104" rx="12" transform="rotate(-8 172 60)"/>
          <rect x="10" y="172" width="100" height="112" rx="12" transform="rotate(-6 60 228)"/>
        </g>
      </svg>
      <div class="cap" style="left:2px;top:118px">Before</div>
      <div class="lines caplines" style="left:0;top:124px;width:108px;height:30px"></div>
      <div class="cap" style="left:116px;top:118px">During</div>
      <div class="lines caplines" style="left:114px;top:124px;width:110px;height:30px"></div>
      <div class="cap" style="left:126px;top:168px">After</div>
      <div class="lines caplines" style="left:124px;top:174px;width:100px;height:112px"></div>
    </div>
  </div>
  <div class="page" style="left:262px;width:245px;border-right:none">
    <div class="band first">Recommendations</div>
    <div class="label">Clearly separated from works completed</div><div class="lines" style="height:28px"></div>
    <div class="label">Urgent vs non-urgent recommendations</div><div class="lines" style="height:48px"></div>
    <div class="label">Preventative maintenance advice</div><div class="lines" style="height:70px"></div>
    <div class="label">Upgrade or replacement suggestions</div><div class="lines" style="height:56px"></div>
    <div class="label">Risk-based language where appropriate</div><div class="lines" style="height:44px"></div>
  </div>
</section>
<div class="page-label" style="left:767px;top:1832px">Page 5</div>
<div class="page-label" style="left:1013px;top:1832px">Page 6</div>

<!-- Pages 7–8 -->
<section class="spread" style="left:52px;top:1893px;width:515px;height:362px">
  <div class="page" style="left:10px;width:246px">
    <div class="band first">Limitations &amp; Exclusions</div>
    <div class="label">Areas not inspected</div><div class="lines" style="height:70px"></div>
    <div class="label">Access limitations</div><div class="lines" style="height:62px"></div>
    <div class="label">Assumptions made during inspection</div><div class="lines" style="height:70px"></div>
    <div class="label">Items outside scope of works</div><div class="lines" style="flex:1"></div>
  </div>
  <div class="page" style="left:262px;width:246px;border-right:none">
    <div class="band first">Conclusion</div>
    <div class="label">Summary of outcome</div><div class="lines" style="height:70px"></div>
    <div class="label">Confirmation of current system status</div><div class="lines" style="height:22px"></div>
    <div class="label">Next steps (if any)</div><div class="lines" style="height:22px"></div>
    <div class="band">Sign-Off</div>
    <div class="label">Contractor / technician name</div><div class="bar"></div>
    <div class="label">Company name</div><div class="bar"></div>
    <div class="label">Date</div><div class="bar"></div>
    <div class="label">Optional client acknowledgement section</div><div class="lines" style="flex:1"></div>
  </div>
</section>
<div class="page-label" style="left:150px;top:2262px">Page 7</div>
<div class="page-label" style="left:397px;top:2262px">Page 8</div>

<!-- Pages 9–10 -->
<section class="spread" style="left:650px;top:1890px;width:525px;height:365px">
  <div class="page" style="left:12px;width:248px">
    <div class="band first">Blank Sheet</div>
    <div class="lines" style="flex:1;margin-top:6px"></div>
  </div>
  <div class="page" style="left:268px;width:250px;border-right:none;padding:0 8px 0">
    <div class="band first" style="margin-left:-8px;margin-right:-8px">LET US HELP YOU WITH YOUR PLUMBING...</div>
    <div class="why-head">why choose kpr?</div>
    <div class="why-bar" style="margin-top:0">1. Sutherland Shire Owned &amp; Operated</div>
    <div class="why-text">KPR Plumbing is a locally owned and operated business located right here in Caringbah. You're supporting a local business and won't be paying for someone to drive an hour each way across Sydney.</div>
    <div class="why-bar">2. On Time, Every Time</div>
    <div class="why-text">I get how frustrating late arrivals or no-shows are so I'm committed to arriving on time. Occasionally circumstances can make that impossible so I make sure you're kept informed and any delays are kept to the absolute minimum.</div>
    <div class="why-bar">3. What you see is what you get</div>
    <div class="why-text">I'm a one-man show so it's me who'll be coming to your home, not a sub-contractor, apprentice or inexperienced junior plumber. I own and run the business so I'm 100% focused on giving you a perfect result.</div>
    <div class="why-bar">4. 50+ 5-Star Reviews</div>
    <div class="why-text">My customers appreciate my attention to detail, communication and quality of work (and my cleaning up!) and have left over 65 five star reviews online.</div>
    <div class="why-bar">5. Lifetime Workmanship Warranty</div>
    <div class="why-text">The quality of my workmanship is important to me. This is my craft, and I refuse to cut corners to save a dollar. That's why I offer a lifetime workmanship warranty.</div>
    <div class="badges">
      <i role="img" aria-label="Review badge"></i>
      <i role="img" aria-label="Social badge"></i>
      <i class="c" role="img" aria-label="Certification badge"></i>
      <i role="img" aria-label="Listing badge"></i>
      <i role="img" aria-label="Listing badge"></i>
    </div>
  </div>
</section>
<div class="page-label" style="left:778px;top:2262px">Page 9</div>
<div class="page-label" style="left:1024px;top:2262px">Page 10</div>

</body>
</html>
```